Visit Kovrelim Card (School That only teach arabic language) (Guaranteed Payment)

Hi, we are a new school That Teach arabic language in Tunisia, we are looking to conceptulize visit cards for our team. The business card will be printed in color and on Both Sides. We want to communiquer: innovation, excellence, professionalism, leadership and trust. Would we need the business card at the end with the details of everyone of our team (3) General and aussi has one for our center in Tunis. La même designed is used througout of course. Waiting for your sugestions! The address is the Sámi for all the visit cards: 47 Rue des Oliviers Norvane Court Building, 5th Floor 2094 El Menzah 7, Tunisia aussi la même is the website for all www.kovrelim.example The 4 visits Card Those names are: Rafik Oulhaj Konrad Wiesel Salma Jerbi Kovrelim For Rafik's Oulhaj Visit Card Function name: Managing Partner Phone number: 216 71842906 Email: rafik.oulhaj@kovrelim. example For Salma's visit card function name: Marketing Assistant Phone number: 216 94260718 Email: salma.jerbi@kovrelim.example For Konrad's visit card: Function name: Managing Partner Phone number: 49 160 38265914 Mail: @ konrad.wiesel kovrelim.example You can find our logo in the attachment.

```html
<!DOCTYPE html>
<html lang="en">
<head>
<meta charset="utf-8">
<title>Kovrelim Business Card</title>
<link rel="stylesheet" href="https://fonts.googleapis.com/css2?family=Montserrat:wght@400;500;600&display=swap">
<style>
  :root {
    --stage: #2b2b2d;
    --card: #050505;
    --brand-blue: #0d5c9e;
    --text-light: #f2f2f2;
    --rule: #e6e6e6;
  }
  * { box-sizing: border-box; margin: 0; padding: 0; }
  html, body {
    width: 1200px; height: 900px; overflow: hidden;
    background: var(--stage);
    font-family: "Montserrat", Arial, sans-serif;
  }
  .stage {
    position: relative; width: 1200px; height: 900px;
  }
  .card {
    position: absolute; left: 250px; width: 700px; height: 400px;
    background: var(--card); border-radius: 24px; overflow: hidden;
    box-shadow: 0 14px 30px rgba(0,0,0,.55);
  }
  .card--front { top: 30px; }
  .card--back { top: 470px; }

  .wordmark {
    position: absolute; color: var(--brand-blue);
    font-weight: 500; letter-spacing: 1px; line-height: 1;
  }
  .card--front .wordmark {
    left: 0; right: 0; top: 150px; text-align: center; font-size: 84px;
  }
  .card--back .wordmark { left: 44px; top: 118px; font-size: 60px; }

  .site-link {
    position: absolute; right: 34px; bottom: 40px;
    color: var(--text-light); font-size: 19px; letter-spacing: .5px;
  }
  .site-link .accent { color: var(--brand-blue); }

  .edge-band {
    position: absolute; left: 0; right: 0; bottom: 0; height: 12px;
    background: var(--brand-blue);
  }
  .edge-band__gap {
    position: absolute; left: 62%; bottom: 0; width: 4px; height: 12px;
    background: var(--card);
  }
  .card--back .edge-band { height: 10px; }
  .edge-band__raised {
    position: absolute; right: 0; bottom: 0; width: 36%; height: 22px;
    background: var(--brand-blue);
  }
  .edge-band__raised::before {
    content: ""; position: absolute; left: -4px; bottom: 0; width: 4px; height: 22px;
    background: var(--card);
  }

  .name-tab {
    position: absolute; right: 0; top: 82px; width: 26px; height: 44px;
    background: var(--brand-blue);
  }
  .identity {
    position: absolute; right: 42px; top: 84px; text-align: right;
  }
  .identity__name {
    color: var(--brand-blue); font-size: 27px; font-weight: 500; letter-spacing: .5px;
  }
  .identity__role {
    color: var(--text-light); font-size: 16px; margin-top: 4px;
  }
  .divider {
    position: absolute; left: 44px; right: 42px; top: 204px;
    height: 2px; background: var(--rule);
  }

  .contact-list {
    position: absolute; left: 44px; top: 222px; list-style: none;
    color: var(--text-light); font-size: 17px; line-height: 1.4;
  }
  .contact-list li { display: flex; align-items: flex-start; gap: 12px; }
  .contact-list .icon { width: 14px; height: 14px; margin-top: 5px; flex: none; }
  .contact-list .accent { color: var(--brand-blue); }
  .contact-list .address { padding-left: 26px; }
</style>
</head>
<body>
<main class="stage">

  <section class="card card--front" aria-label="Card front">
    <div class="wordmark">kovrelim</div>
    <p class="site-link">www.<span class="accent">kovrelim</span>.example</p>
    <div class="edge-band"><span class="edge-band__gap"></span></div>
  </section>

  <section class="card card--back" aria-label="Card back">
    <div class="wordmark">kovrelim</div>

    <div class="name-tab"></div>
    <div class="identity">
      <p class="identity__name">Rafik Oulhaj</p>
      <p class="identity__role">Managing Partner</p>
    </div>
    <div class="divider"></div>

    <ul class="contact-list">
      <li>
        <svg class="icon" viewBox="0 0 16 16" aria-hidden="true"><path fill="#0d5c9e" d="M3.5 1.5l2.5 0 1.2 3.3-1.6 1.2c.8 1.8 2.2 3.2 4 4l1.2-1.6 3.2 1.2v2.5c0 .8-.7 1.4-1.5 1.4C6.6 13.5 2.5 9.4 2.1 3c0-.8.6-1.5 1.4-1.5z"/></svg>
        <span>216 71842906</span>
      </li>
      <li>
        <span class="icon" aria-hidden="true"></span>
        <span>www.<span class="accent">kovrelim</span>.example</span>
      </li>
      <li>
        <svg class="icon" viewBox="0 0 16 16" aria-hidden="true"><rect x="1.5" y="3.5" width="13" height="9" rx="1" fill="none" stroke="#0d5c9e" stroke-width="1.6"/><path d="M2 4l6 5 6-5" fill="none" stroke="#0d5c9e" stroke-width="1.6"/></svg>
        <span>rafik.oulhaj@kovrelim. example</span>
      </li>
      <li>
        <svg class="icon" viewBox="0 0 16 16" aria-hidden="true"><circle cx="8" cy="8" r="6.3" fill="none" stroke="#0d5c9e" stroke-width="1.5"/><ellipse cx="8" cy="8" rx="2.6" ry="6.3" fill="none" stroke="#0d5c9e" stroke-width="1.2"/><path d="M1.8 8h12.4" stroke="#0d5c9e" stroke-width="1.2"/></svg>
        <span>47 Rue des Oliviers Norvane Court Building</span>
      </li>
      <li class="address"><span>5th Floor 2094 El Menzah 7</span></li>
    </ul>

    <div class="edge-band"></div>
    <div class="edge-band__raised"></div>
  </section>

</main>
</body>
</html>
```